Fibromyalgia course needing google word doc design for content for course takers

We are in need of a google word doc design for new course for content please see attached logo for colors and look

```html
<!DOCTYPE html>
<html lang="en">
<head>
<meta charset="utf-8">
<title>Steady Ease – Course Workbook Pages</title>
<link rel="stylesheet" href="https://fonts.googleapis.com/css2?family=Didact+Gothic&family=Roboto+Condensed:wght@700&display=swap">
<style>
  :root{
    --stage:#1c1c1e;
    --paper:#ffffff;
    --purple:#7b2c8f;
    --magenta:#c1218b;
    --ink:#555257;
    --ink-soft:#777479;
    --rule:#d7cfe0;
    --photo-a:#d9cfc8;
    --photo-b:#8f7f86;
  }
  *{box-sizing:border-box;margin:0;padding:0}
  html,body{width:1200px;height:449px;overflow:hidden;background:var(--stage)}
  body{position:relative;font-family:"Didact Gothic",sans-serif;color:var(--ink)}
  .page{position:absolute;top:50px;width:249px;height:349px;background:var(--paper);overflow:hidden}
  .page--cover{left:53px}.page--welcome{left:335px}.page--about{left:614px}.page--closing{left:899px}
  .abs{position:absolute}
  .photo{position:absolute;background:linear-gradient(135deg,var(--photo-a),var(--photo-b))}
  .photo--circle{border-radius:50%}
  .ring-purple{border:3px solid var(--purple)}
  .ring-magenta{border:3px solid var(--magenta)}
  .brand{font-size:10px;color:var(--purple);white-space:nowrap}
  .band{position:absolute;color:#fff;display:flex;align-items:center;justify-content:center}
  .band--profile{left:110px;top:208px;width:139px;height:23px;background:var(--purple);font-size:12.5px;justify-content:flex-start;padding-left:5px}
  .band--welcome{left:7px;top:11px;width:234px;height:17px;background:var(--magenta);border-radius:5px;font-size:14px}
  .band--topic{left:9px;top:14px;width:231px;height:15px;background:var(--magenta);border-radius:4px;font-family:"Roboto Condensed",sans-serif;font-weight:700;font-size:12px}
  .subtitle{left:110px;top:237px;width:139px;text-align:center;color:var(--magenta);font-size:5.8px;line-height:7.3px}
  .intro{right:8px;top:291px;text-align:right;font-size:6px;line-height:7.5px;color:#333}
  .icon{position:absolute;top:320px;width:10px;height:10px;border-radius:50%;background:var(--magenta)}
  .icon-cap{position:absolute;top:333px;width:30px;font-size:1.8px;line-height:2.2px;text-align:center;color:#333}
  .copy{font-size:4.3px;line-height:5.6px;color:var(--ink-soft)}
  .copy p+p{margin-top:4px}
  .center{text-align:center}
  .justify{text-align:justify}
  .kicker{font-size:6.6px;line-height:7.8px;color:var(--ink-soft);text-transform:uppercase}
  .display{color:var(--magenta);font-size:11.5px;text-transform:uppercase;white-space:nowrap}
  .site{position:absolute;left:10px;top:336px;font-size:4.6px;letter-spacing:1.5px;color:var(--purple);display:flex;align-items:center;gap:2px;width:210px}
  .site::after{content:"";flex:1;height:.5px;background:var(--magenta)}
  .label{font-size:5.5px;color:var(--ink-soft)}
  .label b{color:var(--purple);font-weight:400}
  .lead{color:var(--magenta);font-size:7px;line-height:8.4px}
  .checks{list-style:none}
  .checks li{display:flex;align-items:center;gap:5px;white-space:nowrap;color:var(--ink-soft)}
  .checks svg{width:5px;height:5px;flex:none}
  .checks--large li{font-size:7.3px;height:15.7px}
  .checks--ruled li{font-size:6px;height:13.5px;border-bottom:.8px solid var(--rule)}
  .question{font-family:"Roboto Condensed",sans-serif;font-weight:700;color:var(--purple);font-size:10px;line-height:12.6px;text-transform:uppercase}
  .thanks{color:var(--purple);font-size:22px;line-height:1;white-space:nowrap}
  .brand--large{font-size:19px}
</style>
</head>
<body>

<!-- Cover -->
<section class="page page--cover">
  <div class="abs brand" style="left:13px;top:62px">Steady Ease</div>
  <div class="photo photo--circle ring-magenta" style="left:110px;top:82px;width:126px;height:126px" role="img" aria-label="Therapist massaging a young man's neck and shoulder"></div>
  <div class="photo photo--circle ring-purple" style="left:34px;top:132px;width:74px;height:74px" role="img" aria-label="Clinician examining a senior woman's neck"></div>
  <div class="photo photo--circle ring-magenta" style="left:20px;top:208px;width:88px;height:88px" role="img" aria-label="Physiotherapist treating a woman's shoulder"></div>
  <div class="band band--profile">COMPANY PROFILE</div>
  <p class="abs subtitle">COMPLIANCE, PLANNING, MANAGEMENT<br>INNOVATION FUNDING, MARKET</p>
  <p class="abs intro">Lorem ipsum dolor sit amet,<br>consectetuer adipiscing elit,<br>sed diam nonummy nibh</p>
  <span class="icon" style="left:166px"></span>
  <span class="icon" style="left:194px"></span>
  <span class="icon" style="left:223px"></span>
  <p class="icon-cap" style="left:156px">Lorem ipsum dolor sit amet, consectetuer adipiscing elit, sed diam nibh</p>
  <p class="icon-cap" style="left:184px">Lorem ipsum dolor sit amet, consectetuer adipiscing elit, sed diam nibh</p>
  <p class="icon-cap" style="left:213px">Lorem ipsum dolor sit amet, consectetuer adipiscing elit, sed diam nibh</p>
</section>

<!-- Welcome -->
<section class="page page--welcome">
  <div class="band band--welcome">WELCOME!</div>
  <div class="abs copy center" style="left:10px;top:34px;width:229px">
    <p>Lorem ipsum dolor sit amet, consectetuer adipiscing elit, sed diam nonummy nibh euismod tincidunt ut laoreet dolore magna aliquam erat volutpat. Ut wisi enim ad minim veniam, quis nostrud exerci tation ullamcorper suscipit lobortis nisl ut aliquip ex ea commodo consequat. Duis autem vel eum iriure dolor in hendrerit in vulputate velit esse molestie consequat, vel illum dolore eu feugiat nulla facilisis at vero eros et accumsan et iusto odio dignissim qui</p>
    <p>blandit praesent luptatum zzril delenit augue duis dolore te feugait nulla facilisi.<br>Lorem ipsum dolor sit amet, cons ectetuer adipiscing elit, sed diam nonummy nibh euismod tincidunt ut laoreet dolore magna aliquam erat volutpat.</p>
    <p>Ut wisi enim ad minim veniam, quis nostrud exerci tation ullamcorper suscipit lobortis nisl ut aliquip ex ea commodo consequat.</p>
    <p>blandit praesent luptatum zzril delenit augue duis dolore te feugait nulla facilisi.<br>Lorem ipsum dolor sit amet, cons ectetuer adipiscing elit, sed diam nonummy aliquam erat volutpat.</p>
  </div>
  <p class="abs kicker" style="left:10px;top:125px">We are very young<br>studio based in we love to</p>
  <p class="abs display" style="left:10px;top:141px">Creative things</p>
  <div class="abs copy justify" style="left:10px;top:157px;width:93px">
    <p>Lorem Ipsum is simply dummy text of the printing and typesetting industry. Lorem Ipsum has been the industry's standard dummy text ever since the 1500s, when an unknown printer took a galley of type and</p>
    <p>scrambled it to make a type specimen book. It has survived not only five centuries, but also the leap into electronic typesetting, remaining essentially unchanged.</p>
    <p>It was popularised in the 1960s with the release of Glyphset sheets containing Lorem Ipsum passages, and more recently with desktop publishing software like Folio Maker including versions of Lorem Ipsum.</p>
    <p>Lorem Ipsum is simply dummy text of the printing and typesetting industry. Lorem Ipsum has been the industry's standard dummy text ever since the 1500s, when an unknown printer took a galley of type and</p>
    <p>Lorem Ipsum is simply dummy text of the printing and typesetting industry. Lored unknown printer took a galley of type.</p>
  </div>
  <div class="photo" style="left:113px;top:124px;width:126px;height:178px;border-radius:9px;background:linear-gradient(160deg,#e6ebee,#9aa7b4 55%,#3a3f57)" role="img" aria-label="Woman holding her head in discomfort while a doctor and nurse review notes behind her"></div>
  <p class="site">www.yourwebsite.com</p>
</section>

<!-- About -->
<section class="page page--about">
  <div class="band band--topic">DOLOR NAM LIBER AT VERO SOLUTA NOBIS</div>
  <div class="abs copy justify" style="left:9px;top:33px;width:231px;font-size:3.7px;line-height:4.8px">
    <p>Lorem Ipsum is simply dummy text of the printing and typesetting industry. Lorem Ipsum has been the industry's standard dummy text ever since the 1500s, when an unknown printer took a galley of type and scrambled it to make a type specimen book. It has survived not only five centuries, but also the leap into electronic typesetting, remaining essentially unchanged. It was popularised in the 1960s with the release of Glyphset sheets containing Lorem Ipsum passages, and more recently with desktop publishing software like Folio Maker including versions of Lorem Ipsum.</p>
    <p>ook. It has survived not only five centuries, but also the leap into electronic typesetting, remaining essentially unchanged. It was popularised in the 1960s with the release of Glyphset sheets containing Lorem Ipsum passages, and more recently with desktop publishing software like Folio Maker including versions of Lorem Ipsum.</p>
    <p>remaining essentially unchanged. It was popularised in the 1960s with the release of Glyphset sheets containing Lorem Ipsum passages, and more recently with desktop publishing software like Folio Maker including versions of Lorem Ipsum.</p>
  </div>
  <p class="abs kicker" style="left:9px;top:105px;font-size:7.6px;line-height:9.4px">We are very young<br>studio based in we love to</p>
  <p class="abs display" style="left:9px;top:124px;font-size:14px">Creative things</p>
  <div class="abs copy justify" style="left:9px;top:149px;width:110px;font-size:3.4px;line-height:4.3px">
    <p>Lorem Ipsum is simply dummy text of the printing and typesetting industry. Lorem Ipsum has been the industry's standard dummy text ever since the 1500s, when an unknown printer took a galley of type and</p>
    <p>scrambled it to make a type specimen book. It has survived not only five centuries, but also the leap into electronic typesetting, remaining essentially unchanged.</p>
    <p>It was popularised in the 1960s with the release of Glyphset sheets containing Lorem Ipsum passages, and more recently with desktop publishing software like Folio Maker including versions of Lorem Ipsum.</p>
  </div>
  <div class="abs" style="left:132px;top:106px;width:108px;border-left:.5px solid var(--rule);padding-left:2px">
    <p class="label">ABOUT <b>US</b></p>
    <p class="copy justify" style="font-size:3.5px;line-height:4.6px;margin-top:1px">Lorem Ipsum is simply dummy text of the printing and typesetting industry. Lorem Ipsum has been the industry's standard dummy text ever since the 1500s, when an unknown printer took a galley of type and scrambled it to make a type specimen book. It has survived not only five centuries, but also the leap into electronic typesetting, remaining essentially unchanged.</p>
    <p class="label" style="margin-top:12px">OUT <b>TARGET</b></p>
    <p class="copy justify" style="font-size:3.5px;line-height:4.6px;margin-top:1px">Lorem Ipsum is simply dummy text of the printing and typesetting industry. Lorem Ipsum has been the industry's standard dummy text ever since the 1500s, when an unknown printer took a galley of type and scrambled it to make a type specimen book. It has survived not only five centuries, but also the leap into electronic typesetting, remaining essentially unchanged.</p>
  </div>
  <p class="abs lead" style="left:9px;top:214px">And your online busines<br>needs one. Just make sure it:</p>
  <ul class="abs checks checks--large" style="left:9px;top:238px">
    <li><svg viewBox="0 0 10 10"><path d="M1 5.5l3 3L9 1" fill="none" stroke="#8a8a8a" stroke-width="1.4"/></svg>Fits your business or products</li>
    <li><svg viewBox="0 0 10 10"><path d="M1 5.5l3 3L9 1" fill="none" stroke="#8a8a8a" stroke-width="1.4"/></svg>Is easy to spell and remember</li>
    <li><svg viewBox="0 0 10 10"><path d="M1 5.5l3 3L9 1" fill="none" stroke="#8a8a8a" stroke-width="1.4"/></svg>Fits your business or products</li>
    <li><svg viewBox="0 0 10 10"><path d="M1 5.5l3 3L9 1" fill="none" stroke="#8a8a8a" stroke-width="1.4"/></svg>Is easy to spell and remember</li>
  </ul>
  <p class="abs question" style="left:129px;top:210px">What's a domain?<br>It's that name up i<br>the address bar.</p>
  <ul class="abs checks checks--ruled" style="left:129px;top:254px;width:120px">
    <li><svg viewBox="0 0 10 10"><path d="M1 5.5l3 3L9 1" fill="none" stroke="#8a8a8a" stroke-width="1.4"/></svg>Fits your business or products</li>
    <li><svg viewBox="0 0 10 10"><path d="M1 5.5l3 3L9 1" fill="none" stroke="#8a8a8a" stroke-width="1.4"/></svg>Is easy to spell and remember</li>
    <li><svg viewBox="0 0 10 10"><path d="M1 5.5l3 3L9 1" fill="none" stroke="#8a8a8a" stroke-width="1.4"/></svg>Fits your business or products</li>
  </ul>
  <p class="site">www.yourwebsite.com</p>
</section>

<!-- Closing -->
<section class="page page--closing">
  <div class="abs brand brand--large" style="left:0;width:249px;top:120px;text-align:center">Steady Ease</div>
  <div class="photo photo--circle ring-magenta" style="left:69px;top:172px;width:82px;height:82px" role="img" aria-label="Therapist massaging a young man's neck and shoulder"></div>
  <div class="photo photo--circle ring-purple" style="left:19px;top:206px;width:48px;height:48px" role="img" aria-label="Clinician examining a senior woman's neck"></div>
  <div class="photo photo--circle ring-magenta" style="left:9px;top:256px;width:58px;height:58px" role="img" aria-label="Physiotherapist treating a woman's shoulder"></div>
  <p class="abs thanks" style="left:72px;top:256px">THANK YOU</p>
  <div class="abs copy" style="left:72px;top:281px;width:164px;font-size:4.3px;line-height:5.2px;color:#666">
    <p>Lorem ipsum dolor sit amet, consectetuer adipiscing elit, sed diam nonummy nibh euismod tincidunt ut laoreet dolore magna aliquam erat volutpat. Ut wisi enim ad minim veniam,</p>
    <p>quis nostrud exerci tation ullamcorper suscipit lobortis nisl ut aliquip ex ea commodo consequat. Duis autem vel eum iriure dolor in hendrerit in vulputate velit esse molestie consequat, vel illum dolore eu</p>
  </div>
</section>

</body>
</html>
```